Nobody Left the Lantern Burning - Tom Halvery - CD Cover Design Project

Single Cover for CD & Online media e.g. Tunebox Graphics
The first song release from Tom Halvery will be the track 'Nobody Left the Lantern Burning'.
For the release the single requires artwork that is eye catching, seriously professional & meets the requirements of Disc Sprout, Tunebox and also a physical copy on CD.
Track listings for CD will be:
1. Nobody Left the Lantern Burning
2. Nobody Left the Lantern Burning - Instrumental
see details in this link:
http://members.discsprout-example.com/faq.aspx
http://selfmadesound.discsprout-example.com/2009/11/avoid-album-art-atrocities/
http://answers.quorvex-example.com/question/index?qid=20111015141433AAdDTmH
Any advice on this would be greatly appreciated,
I would also like the two logo's I have uploaded to be used,
one is the Tom Halvery logo and the other is for Milbrook & Tandy Records logo (please remove the R and replace with a C for copyright.)
There are four high res photo shopped pictures of Tom Halvery and another zip file of many others, it would be nice to include one of these maybe on the 2nd page or back of the CD. Please don't use them as the front cover.
I imagine an Art Deco illustration but please listen to the track and let it inspire you.
Good Luck
Updates
I don't feel this is what I'm looking for, the design needs to refelct a broken heart without being a picture of a broken heart
Reason: No design has been what we are after so far so the deadline has been extended and the budget increased.

```html
<!DOCTYPE html>
<html lang="en">
<head>
<meta charset="utf-8">
<title>Nobody Left the Lantern Burning – Tom Halvery</title>
<link href="https://fonts.googleapis.com/css2?family=Pinyon+Script&family=Montserrat:ital,wght@1,600&display=swap" rel="stylesheet">
<style>
  :root {
    --glow-cream: #fff6cf;
    --glow-peach: #ffd39a;
    --ember-orange: #f08a4a;
    --ember-red: #d83a2e;
    --dusk-magenta: #8a2f6a;
    --night-violet: #2c1a4a;
    --title-ink: #fff3e4;
    --label-ink: #f6dccb;
  }
  html, body {
    margin: 0;
    padding: 0;
    width: 1200px;
    height: 1200px;
    overflow: hidden;
    background: var(--night-violet);
  }
  .cover {
    position: relative;
    width: 1200px;
    height: 1200px;
    overflow: hidden;
  }
  .cover-photo {
    position: absolute;
    inset: 0;
    background:
      radial-gradient(ellipse 520px 360px at 620px 130px, var(--glow-cream) 0%, rgba(255,230,180,0.85) 45%, rgba(255,200,140,0) 100%),
      radial-gradient(ellipse 700px 650px at 1050px 450px, rgba(245,160,90,0.9) 0%, rgba(240,140,80,0) 75%),
      radial-gradient(ellipse 520px 600px at 120px 420px, rgba(216,58,46,0.95) 0%, rgba(216,58,46,0) 80%),
      radial-gradient(ellipse 900px 700px at 80px 1150px, var(--night-violet) 0%, rgba(44,26,74,0) 75%),
      radial-gradient(ellipse 600px 500px at 1150px 1150px, rgba(40,30,80,0.9) 0%, rgba(40,30,80,0) 80%),
      linear-gradient(180deg, var(--glow-peach) 0%, var(--ember-orange) 40%, #b4504a 65%, var(--dusk-magenta) 85%, var(--night-violet) 100%);
  }
  .release-title {
    position: absolute;
    left: 0;
    width: 1200px;
    top: 556px;
    margin: 0;
    text-align: center;
    font-family: "Pinyon Script", cursive;
    font-weight: 400;
    font-size: 60px;
    line-height: 1;
    color: var(--title-ink);
    text-shadow: 0 1px 3px rgba(90, 30, 30, 0.35);
  }
  .artist-name {
    position: absolute;
    right: 236px;
    top: 632px;
    margin: 0;
    font-family: "Montserrat", sans-serif;
    font-style: italic;
    font-weight: 600;
    font-size: 21px;
    line-height: 1.2;
    color: var(--title-ink);
  }
  .artist-label {
    position: absolute;
    left: 0;
    width: 1200px;
    top: 770px;
    margin: 0;
    text-align: center;
    font-family: "Montserrat", sans-serif;
    font-style: italic;
    font-weight: 600;
    font-size: 26px;
    line-height: 1.2;
    color: var(--label-ink);
  }
</style>
</head>
<body>
  <main class="cover">
    <div class="cover-photo" role="img" aria-label="Warm hazy photograph of wooden stairs with a pair of red canvas sneakers on a step, washed in glowing bokeh light"></div>
    <h1 class="release-title">“Nobody Left the Lantern Burning”</h1>
    <p class="artist-name">Tom Halvery</p>
    <p class="artist-label">Harrow Vale</p>
  </main>
</body>
</html>
```